Kestrel Homes Web Site Design

improve on the graphic design on our current website
www.kestrelhmoes.com.au
wordpress required

Industry/Entity Type

Graphic Design

Coding

Coded - Design and coding required

Number of Pages Required

5+ page

```html
<!DOCTYPE html>
<html lang="en">
<head>
<meta charset="utf-8">
<title>Kestrel Homes</title>
<link href="https://fonts.googleapis.com/css2?family=Roboto:wght@300;400&display=swap" rel="stylesheet">
<style>
:root{
  --red:#c8202f;
  --red-text:#d42a35;
  --topbar:#0d1114;
  --panel:rgba(8,10,12,.86);
  --section:#1f1d1e;
  --footer:#0b0b0c;
  --white:#ffffff;
  --muted:#bdbdbd;
}
*{margin:0;padding:0;box-sizing:border-box}
html,body{width:1200px;height:900px;overflow:hidden;background:#000}
body{font-family:'Roboto',sans-serif;color:var(--white);position:relative}
.topbar{position:absolute;left:0;top:0;width:1200px;height:48px;background:var(--topbar);border-top:2px solid var(--red)}
.phone{position:absolute;left:746px;top:9px;display:flex;align-items:center;gap:10px;font-size:20px;font-weight:400}
.follow{position:absolute;left:921px;top:14px;display:flex;align-items:center;gap:9px;font-size:14px;font-weight:400;letter-spacing:.3px}
.social{width:26px;height:26px;border-radius:50%;background:var(--red);display:inline-block}
.follow .label{margin-right:4px}
.hero{position:absolute;left:0;top:48px;width:1200px;height:581px;
  background:linear-gradient(180deg,#3aa3e0 0%,#7cc6ee 22%,#8e877f 38%,#7a7268 55%,#d9d7d2 68%,#4f5a3a 80%,#6a8a3a 92%,#7a9a44 100%)}
.sidepanel{position:absolute;left:80px;top:48px;width:230px;height:450px;background:var(--panel);border-bottom-right-radius:110px}
.brand{position:absolute;left:38px;top:20px;display:flex;align-items:center;gap:8px}
.brand-mark{width:40px;height:40px;border-radius:50%;border:3px solid var(--red)}
.brand-name{font-size:20px;font-weight:400;color:var(--white);line-height:1}
.brand-sub{position:absolute;left:88px;top:54px;font-size:7px;color:var(--muted)}
.nav{position:absolute;left:38px;top:80px;width:154px;list-style:none}
.nav li{height:43px;display:flex;align-items:center;gap:11px;font-size:14.5px;font-weight:400;border-bottom:1px dotted #6a6a6a}
.nav li:last-child{border-bottom:none}
.nav .dot{width:16px;height:16px;border-radius:50%;border:2px solid #ddd;border-left-color:var(--red);border-bottom-color:var(--red)}
.gallery-btn{position:absolute;left:35px;top:342px;width:162px;height:34px;background:var(--red);border-radius:3px;box-shadow:0 2px 0 #7d0f19;font-size:16px;font-weight:400;display:flex;align-items:center;justify-content:center}
.services{position:absolute;left:0;top:629px;width:1200px;height:224px;background:var(--section)}
.service{position:absolute;top:0;width:260px;text-align:center}
.service .badge{position:absolute;left:72px;top:-58px;width:116px;height:116px;border-radius:50%;background:#0e0e0f;border:2px solid var(--red);display:flex;align-items:center;justify-content:center}
.service h2{position:absolute;top:77px;left:0;width:260px;font-size:18px;font-weight:300;color:var(--red-text)}
.service p{position:absolute;top:113px;left:0;width:260px;font-size:12.5px;font-weight:300;line-height:21px;color:#e6e6e6}
.arrow{position:absolute;top:38px}
.footer{position:absolute;left:0;top:853px;width:1200px;height:47px;background:var(--footer);border-top:2px solid var(--red);font-size:11.5px;font-weight:300;color:var(--muted);display:flex;align-items:center;justify-content:center}
</style>
</head>
<body>
<header class="topbar">
  <div class="phone">
    <svg width="26" height="26" viewBox="0 0 26 26" aria-hidden="true"><circle cx="13" cy="13" r="11.5" fill="none" stroke="#c8202f" stroke-width="2"/><path d="M8 7c1-1 2-1 3 1l1 2c0 1-1 1-1 2 1 2 2 3 4 4 1 0 1-1 2-1l2 1c2 1 2 2 1 3-2 2-5 1-8-2s-5-6-4-10z" fill="#c8202f"/></svg>
    <span>123 456 7710</span>
  </div>
  <div class="follow">
    <span class="label">FOLLOW US :</span>
    <span class="social" role="img" aria-label="Social network link"></span>
    <span class="social" role="img" aria-label="Social network link"></span>
    <span class="social" role="img" aria-label="Social network link"></span>
  </div>
</header>

<div class="hero" role="img" aria-label="Photograph of a grey two-storey family home with white porch columns, red front door and landscaped garden under a blue sky"></div>

<nav class="sidepanel">
  <div class="brand"><span class="brand-mark"></span><span class="brand-name">Kestrel Homes</span></div>
  <div class="brand-sub">Homes &amp; Designs Pty Ltd</div>
  <ul class="nav">
    <li><span class="dot"></span>Home</li>
    <li><span class="dot"></span>About Us</li>
    <li><span class="dot"></span>Excellence</li>
    <li><span class="dot"></span>Experience</li>
    <li><span class="dot"></span>Expertise</li>
    <li><span class="dot"></span>Contact</li>
  </ul>
  <div class="gallery-btn">See Our Gallery</div>
</nav>

<section class="services">
  <svg class="arrow" style="left:30px" width="22" height="40" viewBox="0 0 22 40" aria-hidden="true"><path d="M20 2 2 20l18 18" fill="none" stroke="#c8202f" stroke-width="1.5"/></svg>
  <svg class="arrow" style="left:1148px" width="22" height="40" viewBox="0 0 22 40" aria-hidden="true"><path d="M2 2l18 18L2 38" fill="none" stroke="#c8202f" stroke-width="1.5"/></svg>

  <div class="service" style="left:70px">
    <div class="badge"><svg width="60" height="50" viewBox="0 0 60 50" aria-hidden="true"><path d="M6 24 30 6l24 18v22H6z" fill="#fff"/><rect x="24" y="30" width="12" height="16" fill="#0e0e0f"/></svg></div>
    <h2>Canberra Building Services</h2>
    <p>Kestrel Homes is a Canberra based building company focusing on first class residential homes and 100% client satisfaction.</p>
  </div>
  <div class="service" style="left:337px">
    <div class="badge" role="img" aria-label="Icon of an architect holding plans"></div>
    <h2>Top Class Architects</h2>
    <p>Working with the best architects in Canber-ra, has always been our strength. This ensures our ability to deliver best service.</p>
  </div>
  <div class="service" style="left:603px">
    <div class="badge" role="img" aria-label="Icon of two contractors"></div>
    <h2>Reliable Contractors</h2>
    <p>Working with the best contractors enables us to provide you with construction services that are on time and on budget.</p>
  </div>
  <div class="service" style="left:870px">
    <div class="badge"><svg width="56" height="50" viewBox="0 0 56 50" aria-hidden="true"><rect x="4" y="38" width="8" height="10" rx="1" fill="#fff"/><rect x="16" y="30" width="8" height="18" rx="1" fill="#fff"/><rect x="28" y="34" width="8" height="14" rx="1" fill="#fff"/><rect x="40" y="22" width="8" height="26" rx="1" fill="#fff"/><path d="M4 28 18 16l10 8L48 4" fill="none" stroke="#fff" stroke-width="3"/><path d="M40 2h10v10z" fill="#fff"/></svg></div>
    <h2>30 Years Of Experience</h2>
    <p>Mauris accumsan eros eget libero posuere vulputate. Etiam elit elit, elementum sed varius at, adipiscing vitae est.</p>
  </div>
</section>

<footer class="footer">Copyright@kestrelhomes.com.au. All Rights Are Reserved.</footer>
</body>
</html>
```